BHSC Business cards

We are an established dental practice that is looking for new business cards to match our new logo. We are looking for something unique and sophisticated.
BRIEF: Colours are black, silver and white. Include the company name, logo (including “Pelwick Heath Dental Care”) and phone number “03 9415 2876”.
Front - Include the company name, logo (including “Pelwick Heath Dental Care”) and phone number “03 9415 2876”.
Back - Include the company name,  “Pelwick Heath Dental Care”, phone number “03 9415 2876”. address "64A Tindle Street, Pelwick Heath, Vic 3187", "Email reception@pelwickheathdentalcare.com.au", the Dentist Name " Dr ................................"  Your next appointment "Day, date and time(am/pm)".  3 lines for 3 appointments please, and at the bottom "IF UNABLE TO KEEP THIS APPOINTMENT 48 HOURS NOTICE IS REQUIRED."
Try and be creative and different with the design, i've added an image for inspiration

Target Market(s)
ALL in need of dental
Industry/Entity Type
Dental Clinic
Look and feel
Each slider illustrates characteristics of the customer's brand and the style your logo design should communicate.

```html
<!DOCTYPE html>
<html lang="en">
<head>
<meta charset="utf-8">
<title>Pelwick Heath Dental Care – Business Cards</title>
<link href="https://fonts.googleapis.com/css2?family=Lato:wght@400;700;900&display=swap" rel="stylesheet">
<style>
  :root {
    --backdrop: #e4e4e4;
    --card-black: #121212;
    --card-white: #f5f5f4;
    --silver: #d9d9d9;
    --ink: #1c1c1c;
    --muted: #777777;
    --rule: #3a3a3a;
  }
  * { margin: 0; padding: 0; box-sizing: border-box; }
  html, body {
    width: 1200px; height: 900px; overflow: hidden;
    background: var(--backdrop);
    font-family: "Lato", Arial, sans-serif;
  }
  .canvas { position: relative; width: 1200px; height: 900px; }
  .card {
    position: absolute;
    width: 560px; height: 320px;
    box-shadow: 0 10px 30px rgba(0,0,0,0.18);
  }

  /* Front */
  .card-front {
    left: 80px; top: 110px;
    background: var(--card-black);
    color: var(--silver);
    display: flex; align-items: center; justify-content: center;
  }
  .brand { display: flex; align-items: center; gap: 18px; }
  .brand-mark {
    width: 58px; height: 58px; border-radius: 50%;
    background: var(--silver);
    flex: none;
  }
  .brand-text { display: flex; flex-direction: column; gap: 6px; }
  .brand-name {
    font-weight: 700; font-size: 25px; letter-spacing: 1px;
    text-transform: uppercase; line-height: 1.15;
  }
  .brand-phone {
    font-weight: 700; font-size: 17px; letter-spacing: 2px;
  }

  /* Back */
  .card-back {
    left: 560px; top: 470px;
    background: var(--card-white);
    color: var(--ink);
    display: flex; flex-direction: column;
  }
  .back-body { flex: 1; padding: 26px 30px 0 30px; }
  .back-header {
    display: flex; align-items: center; gap: 18px;
    padding-bottom: 12px;
    border-bottom: 1px solid var(--rule);
  }
  .dentist-name { font-weight: 900; font-size: 24px; letter-spacing: 0.5px; }
  .dentist-role { font-size: 14px; color: var(--muted); margin-top: 2px; }
  .header-divider { width: 1px; height: 44px; background: var(--rule); }
  .contact { font-size: 13px; line-height: 1.55; }
  .appointments { display: flex; gap: 14px; margin-top: 18px; }
  .appt-label {
    font-weight: 400; font-size: 19px; letter-spacing: 1px;
    text-transform: uppercase; white-space: nowrap; padding-top: 2px;
  }
  .appt-lines { display: flex; flex-direction: column; gap: 16px; flex: 1; }
  .appt-line { display: flex; align-items: flex-end; gap: 6px; font-size: 15px; }
  .leader { border-bottom: 2px dotted var(--ink); height: 12px; }
  .leader-date { flex: 1; }
  .leader-time { width: 46px; }
  .notice-band {
    height: 40px; background: var(--card-black); color: #ffffff;
    display: flex; align-items: center; justify-content: center;
    font-size: 12.5px; letter-spacing: 0.6px; text-transform: uppercase;
  }
</style>
</head>
<body>
<main class="canvas">
  <section class="card card-front" aria-label="Business card front">
    <div class="brand">
      <div class="brand-mark"></div>
      <div class="brand-text">
        <span class="brand-name">Pelwick Heath Dental Care</span>
        <span class="brand-phone">03 9415 2876</span>
      </div>
    </div>
  </section>

  <section class="card card-back" aria-label="Business card back">
    <div class="back-body">
      <header class="back-header">
        <div class="dentist">
          <div class="dentist-name">DR. ALAN BRERETON</div>
          <div class="dentist-role">Senior Dentist</div>
        </div>
        <div class="header-divider"></div>
        <div class="contact">
          <div>64A Tindle Street, Pelwick Heath, Vic 3187</div>
          <div>reception@pelwickheathdentalcare.com.au</div>
        </div>
      </header>
      <div class="appointments">
        <div class="appt-label">Next Appointment:</div>
        <div class="appt-lines">
          <div class="appt-line">Date <span class="leader leader-date"></span> At <span class="leader leader-time"></span> am/pm</div>
          <div class="appt-line">Date <span class="leader leader-date"></span> At <span class="leader leader-time"></span> am/pm</div>
          <div class="appt-line">Date <span class="leader leader-date"></span> At <span class="leader leader-time"></span> am/pm</div>
        </div>
      </div>
    </div>
    <footer class="notice-band">If unable to keep this appointment 48 hours notice is required</footer>
  </section>
</main>
</body>
</html>
```